Dental Business Card

I need Dental oriented business cards.
On the front side -
- on the first line, my name:
Dr Marlo Vintner
- on the second line (just underneath):
Doctor of Dental Medicine
- on the third line, or underneath that or in a corner, I would like the address and phone number:
5182 Ch. Birchfield
Montreal QC H2T 4B9
514-629-5074
- other than that i would maybe like a logo of a tooth, but i want it to be subtle and very basic!
- I would like the card to be preferably black or dark grey-ish with the writing in white
On the other side -
- 2-3 lines with the possibility to write the next appointment the box with the lines should be white, with the rest of the card being black

```html
<!DOCTYPE html>
<html lang="en">
<head>
<meta charset="utf-8">
<title>Dr Marlo Vintner – Business Card</title>
<link rel="stylesheet" href="https://fonts.googleapis.com/css2?family=Montserrat:wght@400;500;700&display=swap">
<style>
  :root {
    --canvas: #8a8a8a;
    --card: #1c1c1c;
    --ink-light: #ffffff;
    --ink-muted: #e6e6e6;
    --form-bg: #f4f4f4;
    --form-ink: #1a1a1a;
    --rule: #2a2a2a;
  }
  * { box-sizing: border-box; margin: 0; padding: 0; }
  html, body {
    width: 1200px; height: 1021px; overflow: hidden;
    background: var(--canvas);
    font-family: "Montserrat", Arial, sans-serif;
  }
  .sheet {
    width: 1200px; height: 1021px;
    display: flex; flex-direction: column; align-items: center; justify-content: center;
    gap: 44px;
  }
  .card {
    width: 760px; height: 434px;
    background: var(--card);
    color: var(--ink-light);
    box-shadow: 0 10px 28px rgba(0,0,0,.35);
    position: relative;
  }

  /* Back: appointment side */
  .appointment-title {
    position: absolute; top: 42px; left: 0; right: 0;
    text-align: center; font-weight: 700; font-size: 22px; letter-spacing: .5px;
  }
  .appointment-form {
    position: absolute; top: 86px; left: 70px; right: 70px; height: 216px;
    background: var(--form-bg); color: var(--form-ink);
    padding: 14px 28px 0 28px;
    font-size: 16px;
  }
  .form-row {
    display: flex; align-items: flex-end; height: 62px;
  }
  .form-label { white-space: nowrap; }
  .form-line { border-bottom: 1px solid var(--rule); margin: 0 4px 4px 2px; }
  .form-line.date { flex: 1; }
  .form-line.time { width: 140px; }
  .ampm {
    display: flex; flex-direction: column; line-height: 15px; font-size: 15px; margin-left: 6px;
  }
  .appointment-note {
    position: absolute; top: 330px; left: 0; right: 0;
    text-align: center; font-size: 17px; letter-spacing: .3px;
  }

  /* Front: identity side */
  .identity {
    position: absolute; top: 132px; left: 0; right: 0; text-align: center;
  }
  .doctor-name {
    font-family: "Montserrat", Arial, sans-serif; font-weight: 500;
    font-size: 40px; letter-spacing: .5px;
  }
  .doctor-title {
    font-size: 21px; font-weight: 400; color: var(--ink-muted); margin-top: 6px; letter-spacing: .3px;
  }
  .contact {
    position: absolute; top: 300px; left: 0; right: 0; text-align: center;
  }
  .phone {
    font-size: 24px; display: inline-flex; align-items: center; gap: 10px;
  }
  .phone svg { width: 20px; height: 20px; fill: var(--ink-light); }
  .address { font-size: 19px; margin-top: 6px; color: var(--ink-muted); }
</style>
</head>
<body>
<main class="sheet">
  <section class="card card-back" aria-label="Appointment side">
    <h2 class="appointment-title">NEXT APPOINTMENT</h2>
    <div class="appointment-form">
      <div class="form-row"><span class="form-label">Date:</span><span class="form-line date"></span><span class="form-label">Time:</span><span class="form-line time"></span><span class="ampm"><span>am</span><span>pm</span></span></div>
      <div class="form-row"><span class="form-label">Date:</span><span class="form-line date"></span><span class="form-label">Time:</span><span class="form-line time"></span><span class="ampm"><span>am</span><span>pm</span></span></div>
      <div class="form-row"><span class="form-label">Date:</span><span class="form-line date"></span><span class="form-label">Time:</span><span class="form-line time"></span><span class="ampm"><span>am</span><span>pm</span></span></div>
    </div>
    <p class="appointment-note">If unable to keep an appointment, kindly give 24 hrs. notice.</p>
  </section>

  <section class="card card-front" aria-label="Identity side">
    <div class="identity">
      <h1 class="doctor-name">Dr Marlo Vintner</h1>
      <p class="doctor-title">Doctor of Dental Medicine</p>
    </div>
    <div class="contact">
      <p class="phone">
        <svg viewBox="0 0 24 24" aria-hidden="true"><path d="M6.6 10.8c1.4 2.8 3.8 5.1 6.6 6.6l2.2-2.2c.3-.3.7-.4 1-.2 1.1.4 2.3.6 3.6.6.6 0 1 .4 1 1V20c0 .6-.4 1-1 1C10.6 21 3 13.4 3 4c0-.6.4-1 1-1h3.5c.6 0 1 .4 1 1 0 1.3.2 2.5.6 3.6.1.3 0 .7-.2 1L6.6 10.8z"/></svg>
        514-629-5074
      </p>
      <p class="address">5182 Ch. Birchfield, Montreal QC H2T 4B9</p>
    </div>
  </section>
</main>
</body>
</html>
```